Tradeshow Banner Design (Qty2, 6'H x 2'W)

Brightwell Contractors is an Electrical, Fire Alarm, and Security Contracting company. For tradeshows, we would like 2 vertical Banners to put behind our booth. Our colors are Red, Grey & Black. I would like the Banners to be informative on what services we provide, with some appealing Graphic Design. (bwc-kmo.com)
Slogan: Safeguarding Communities Electrical, Fire & Security Solutions
Target Market(s)
Commercial Construction Clients
Industry/Entity Type
Electrical / Construction
Font styles to use
Other font styles liked:
- Aileron
Colors
EB3D1F
EC4F4E
F09395
F8D3D4
FCEDEE
Requirements
Must have
- Our Logo, Color Scheme, Brief Caption of the services we provide
Nice to have
- Appealing Imagery & a modern/simplistic design

```html
<!DOCTYPE html>
<html lang="en">
<head>
<meta charset="utf-8">
<title>Brightwell Contractors – Pull Up Banners</title>
<link rel="stylesheet" href="https://fonts.googleapis.com/css2?family=Poppins:wght@400;500;600;700;800&display=swap">
<style>
  :root{
    --board:#d6d6d6;
    --ink:#161616;
    --black:#050505;
    --white:#ffffff;
    --red:#eb2a25;
    --red-soft:#ec4f4e;
    --grey-text:#3a3a3a;
    --caption:#333333;
  }
  *{box-sizing:border-box;margin:0;padding:0}
  html,body{width:885px;height:1200px;overflow:hidden;background:var(--board);font-family:"Poppins",sans-serif}
  .board{position:relative;width:885px;height:1200px}

  .banner{position:absolute;width:314px;height:941px;background:var(--black);overflow:hidden;box-shadow:4px 6px 10px rgba(0,0,0,.28)}
  .banner--one{left:100px;top:113px}
  .banner--two{left:464px;top:114px}

  .photo{position:absolute;left:0;top:0;width:100%}
  .banner--one .photo{height:390px;background:linear-gradient(180deg,#8fb1d2 0%,#c9c6c0 22%,#e6c28f 30%,#8a7d66 42%,#56613d 60%,#2a3020 78%,#050505 100%)}
  .banner--two .photo{height:420px;background:linear-gradient(180deg,#e8eef4 0%,#b9c9d8 22%,#5f6e80 40%,#3b4656 58%,#8d7a64 68%,#2a2d33 82%,#050505 100%)}

  .brand{position:absolute;left:47px;top:36px;display:flex;align-items:center;gap:12px}
  .brand__mark{width:50px;height:50px;border-radius:50%;background:var(--red);flex:none}
  .brand__name{font-weight:600;font-size:21px;line-height:1.05;color:var(--ink);letter-spacing:.2px;text-transform:uppercase;white-space:nowrap}

  .petal{position:absolute;width:112px;height:112px;border-radius:50%;border:4px solid var(--white);background:linear-gradient(135deg,#d9d9d9,#8a8a8a)}
  .petal--top{left:102px;top:218px;background:linear-gradient(135deg,#f1f1f1,#bdbdbd)}
  .petal--left{left:17px;top:303px;background:linear-gradient(135deg,#f3f3f3,#d33a30)}
  .petal--right{left:186px;top:303px;background:linear-gradient(135deg,#9aa3ad,#3d4650)}
  .petal--bottom{left:102px;top:387px;background:linear-gradient(135deg,#6d7680,#2c2f33)}

  .badge{position:absolute;border:3px solid var(--white);background:var(--black)}
  .badge--square{border-radius:7px}
  .badge--round{border-radius:50%;background:#2a2a2a}

  .headline{position:absolute;left:0;width:100%;text-align:center;font-weight:800;text-transform:uppercase;line-height:1.1;white-space:nowrap}
  .headline .red{color:var(--red)}
  .headline .white{color:var(--white)}
  .banner--one .headline{top:527px;font-size:31px;color:var(--red)}
  .banner--two .headline{top:393px;font-size:28.5px}

  .rule{position:absolute;left:50%;width:240px;height:1px;transform:translateX(-50%);background:linear-gradient(90deg,transparent,#7a2a26 30%,#7a2a26 70%,transparent)}

  .tagline{position:absolute;left:0;top:615px;width:100%;text-align:center;color:var(--white);font-weight:500;font-size:21.5px;line-height:1.05}

  .services{position:absolute;left:27px;top:703px;width:262px;height:114px;border:1.5px solid var(--red);border-radius:8px}
  .services__title{position:absolute;left:50%;top:-12px;transform:translateX(-50%);background:var(--black);padding:0 10px;color:var(--white);font-weight:700;font-size:16.5px;white-space:nowrap}
  .services__title::before,.services__title::after{content:"";position:absolute;top:50%;width:5px;height:5px;border:1.5px solid var(--red);border-radius:50%;transform:translateY(-50%)}
  .services__title::before{left:-2px}
  .services__title::after{right:-2px}
  .service{position:absolute;display:flex;align-items:center;gap:7px;color:var(--white);font-size:13.2px;line-height:1.2;white-space:nowrap}
  .service__icon{width:27px;height:27px;border-radius:50%;background:var(--red);border:2px solid var(--white);flex:none;display:flex;align-items:center;justify-content:center}
  .service--fire{left:12px;top:27px}
  .service--electrical{left:133px;top:27px}
  .service--security{left:12px;top:74px}
  .service--surveillance{left:133px;top:74px}

  .about{position:absolute;left:0;top:556px;width:100%;text-align:center;color:var(--white);font-size:14.6px;line-height:18.6px;padding:0 33px}
  .about p+p{margin-top:6px}

  .contact{position:absolute;left:0;bottom:0;width:100%;height:77px;background:var(--white)}
  .web{position:absolute;left:45px;top:-14px;height:27px;border-radius:14px;background:var(--red);display:flex;align-items:center;padding-right:12px;white-space:nowrap}
  .web__icon{width:30px;height:30px;border-radius:50%;background:var(--white);border:2px solid var(--ink);margin-left:-4px;display:flex;align-items:center;justify-content:center;flex:none}
  .web__url{color:var(--white);font-size:18px;font-weight:500;margin-left:7px;line-height:1;white-space:nowrap}
  .phone{position:absolute;left:0;top:24px;width:100%;text-align:center;color:var(--ink);font-size:26px;font-weight:400;white-space:nowrap}
  .phone b{font-weight:700}

  .label{position:absolute;font-size:11.5px;color:var(--grey-text);transform:rotate(-90deg);transform-origin:left top;white-space:nowrap}
  .label--one{left:69px;top:1056px}
  .label--two{left:801px;top:1056px}
  .caption{position:absolute;left:0;top:1102px;width:100%;text-align:center;font-size:17.5px;color:var(--caption);letter-spacing:.3px}
</style>
</head>
<body>
<main class="board">

  <section class="banner banner--one">
    <div class="photo" role="img" aria-label="Modern apartment buildings at sunset with landscaped grounds"></div>
    <div class="brand"><span class="brand__mark"></span><span class="brand__name">Brightwell<br>Contractors</span></div>

    <div class="petal petal--top" role="img" aria-label="Hand pressing a fire alarm control panel"></div>
    <div class="petal petal--left" role="img" aria-label="Red fire alarm pull station"></div>
    <div class="petal petal--right" role="img" aria-label="Security camera in a warehouse"></div>
    <div class="petal petal--bottom" role="img" aria-label="Electrician wiring an electrical panel"></div>
    <div class="badge badge--square" style="left:251px;top:450px;width:37px;height:37px"></div>

    <h1 class="headline">Safeguarding<br>Communities</h1>
    <div class="rule" style="top:606px"></div>
    <p class="tagline">Electrical, Fire &amp;<br>Security Solutions</p>

    <div class="services">
      <h2 class="services__title">Services We Offer</h2>
      <div class="service service--fire"><span class="service__icon"><svg width="13" height="15" viewBox="0 0 13 15"><path d="M6.5 1C8 4 11 6 11 9.5a4.5 4.5 0 0 1-9 0C2 7 4 6 4 3.5c1 1 1.5 2 2.5 2.5C6.5 4.5 6 2.5 6.5 1z" fill="none" stroke="#fff" stroke-width="1.4"/></svg></span>Fire<br>Protection</div>
      <div class="service service--electrical"><span class="service__icon"><svg width="12" height="15" viewBox="0 0 12 15"><path d="M7 1L2 8.5h4L4.5 14 10 6H6z" fill="#fff"/></svg></span>Electrical<br>System</div>
      <div class="service service--security"><span class="service__icon"><svg width="15" height="12" viewBox="0 0 15 12"><rect x="1" y="2" width="13" height="8" rx="2" fill="none" stroke="#fff" stroke-width="1.4"/><circle cx="7.5" cy="6" r="2" fill="#fff"/></svg></span>Security</div>
      <div class="service service--surveillance"><span class="service__icon"><svg width="13" height="15" viewBox="0 0 13 15"><path d="M6.5 1L12 3v4c0 3.5-2.5 6-5.5 7C3.5 13 1 10.5 1 7V3z" fill="none" stroke="#fff" stroke-width="1.4"/><circle cx="6.5" cy="7" r="1.8" fill="#fff"/></svg></span>Surveillance</div>
    </div>

    <footer class="contact">
      <div class="web"><span class="web__icon"><svg width="18" height="18" viewBox="0 0 18 18"><circle cx="9" cy="9" r="7.5" fill="none" stroke="#161616" stroke-width="1.4"/><ellipse cx="9" cy="9" rx="3.2" ry="7.5" fill="none" stroke="#161616" stroke-width="1.2"/><path d="M1.5 9h15" stroke="#161616" stroke-width="1.2"/></svg></span><span class="web__url">www.bwc-kmo.com</span></div>
      <p class="phone">Call <b>555-014-2286</b></p>
    </footer>
  </section>

  <section class="banner banner--two">
    <div class="photo" role="img" aria-label="City skyscrapers at dusk with a business handshake overlay"></div>
    <div class="brand"><span class="brand__mark"></span><span class="brand__name">Brightwell<br>Contractors</span></div>

    <h1 class="headline"><span class="red">Electrical,<br>Fire &amp; Security</span><br><span class="white">Technology<br>Experts</span></h1>
    <div class="rule" style="top:541px"></div>
    <div class="about">
      <p>As a family business, we have laid a grounded and honest foundation while taking pride in our employees and our work.</p>
      <p>What makes our company so great is most certainly the people here who are dedicated to providing you with the best experience possible.</p>
    </div>
    <div class="rule" style="top:754px"></div>
    <div class="badge badge--round" style="left:112px;top:784px;width:36px;height:36px"></div>
    <div class="badge badge--square" style="left:171px;top:784px;width:36px;height:36px"></div>

    <footer class="contact">
      <div class="web"><span class="web__icon"><svg width="18" height="18" viewBox="0 0 18 18"><circle cx="9" cy="9" r="7.5" fill="none" stroke="#161616" stroke-width="1.4"/><ellipse cx="9" cy="9" rx="3.2" ry="7.5" fill="none" stroke="#161616" stroke-width="1.2"/><path d="M1.5 9h15" stroke="#161616" stroke-width="1.2"/></svg></span><span class="web__url">www.bwc-kmo.com</span></div>
      <p class="phone">Call <b>555-014-2286</b></p>
    </footer>
  </section>

  <span class="label label--one">Pull Up Banner 01</span>
  <span class="label label--two">Pull Up Banner 02</span>
  <p class="caption">Design Concept Brightwell Contractors Banners - 2’x6’</p>
</main>
</body>
</html>
```